Core Value Graphic for a Service Disabled and Minority Certified contractor

My company, Keystone Aid Partners, is a US Federal Contractor that hires veterans and service disabled veterans. Our website is www.keystoneaid7.example. We work hard to maintain a 50:50 split between veterans and non-veterans on our team. Our tagline is "To Find a Better Way." We are continually looking to integrate technology and efficiency into all that we do.

I want a way to express our company core values visually so that our employees and customers alike can read them and get a sense of who we are, what drives us to succeed, and what makes up our team DNA.

I need an artist like you to help me represent our core values visually. In a manner that I can print it out on an 8"X11" sheet of paper or a large 48" X 48" poster, without losing the visual clarity or that it pixelates out of focus. I am looking for a color scheme that is patriotic with Red, White, and Blues and similar hues. I would also like to incorporate my logo and tagline into the design in some manner.

I have attached several examples of a Core Value Grids from other companies. I am hopeful it will inspire you, and a get your brain juices flowing to provide me with a knockout Core Value Grid that will rock only you can provide! I also include a copy of my company Core Values and a copy of our Logo.

Looking forward to seeing your creations. Thanks.

Target Market(s)

Employees, any potential strategic alliance partners, and customers.

Industry/Entity Type

Contractor

Requirements
Must have
• Patriotic feel and have my logo someplace on the document.

```html
<!DOCTYPE html>
<html lang="en">
<head>
<meta charset="utf-8">
<title>Keystone Aid Partners – Our Core Values</title>
<link href="https://fonts.googleapis.com/css2?family=Open+Sans:wght@600;700;800&family=Arimo:wght@700&display=swap" rel="stylesheet">
<style>
  :root{
    --page:#e9e9ea;
    --navy:#1b2145;
    --navy-deep:#141936;
    --blue:#1f3a78;
    --red:#a3161c;
    --red-bright:#c41e24;
    --white:#ffffff;
    --ink:#1a1a1a;
  }
  *{box-sizing:border-box;margin:0;padding:0}
  html,body{width:1200px;height:1000px;overflow:hidden}
  body{background:var(--page);font-family:"Open Sans",Arial,sans-serif;position:relative}

  .poster{position:absolute;left:187px;top:87px;width:810px;height:810px;overflow:hidden;background:var(--navy)}
  .poster-field{position:absolute;left:0;top:100px;width:810px;height:710px;
    background:
      linear-gradient(115deg, rgba(163,22,28,0) 55%, rgba(163,22,28,.55) 72%, rgba(110,16,24,.35) 100%),
      radial-gradient(ellipse at 25% 75%, rgba(120,125,150,.25), rgba(0,0,0,0) 45%),
      linear-gradient(160deg, var(--navy) 0%, var(--navy-deep) 60%, #2a1f3c 100%)}
  .header{position:absolute;left:0;top:0;width:810px;height:100px;
    background:linear-gradient(90deg,#ffffff 0%,#e7e8f0 25%,#8d93b8 50%,#3a3f55 72%,#1d1d22 100%);
    border-bottom:2px solid var(--white)}
  .brand{position:absolute;left:30px;top:39px;display:flex;align-items:center;gap:8px}
  .brand-mark{width:13px;height:13px;background:var(--red)}
  .brand-name{font-weight:700;font-size:18px;color:var(--blue);white-space:nowrap}
  .title{position:absolute;right:32px;top:24px;font-family:"Arimo",Arial,sans-serif;font-weight:700;
    font-size:49px;line-height:56px;color:var(--white);white-space:nowrap;-webkit-text-stroke:1px #3a3f55}
  .footer-rule{position:absolute;left:0;top:800px;width:810px;height:2px;background:rgba(255,255,255,.85)}
  .ghost-title{position:absolute;right:24px;top:740px;font-family:"Arimo",Arial,sans-serif;font-weight:700;
    font-size:50px;color:rgba(255,255,255,.35);white-space:nowrap}

  .connectors{position:absolute;left:0;top:0}

  .value{position:absolute;background:var(--white);padding:8px 8px 6px;text-align:center;color:var(--ink)}
  .value-tab{position:absolute;background:linear-gradient(180deg,var(--red-bright),#7d1015);color:var(--white);
    font-family:"Arimo",Arial,sans-serif;font-size:10.5px;font-weight:700;line-height:12px;text-align:center;
    padding:3px 2px;white-space:nowrap;box-shadow:0 1px 3px rgba(0,0,0,.4)}
  .value h3{font-size:10.5px;font-weight:800;color:var(--red);line-height:13px;margin-top:2px}
  .value p{font-size:8.4px;font-weight:700;text-transform:uppercase;line-height:12.2px}

  .v1{left:93px;top:149px;width:254px;height:217px}
  .t1{left:96px;top:120px;width:120px}
  .v2{left:463px;top:149px;width:257px;height:217px}
  .t2{left:466px;top:121px;width:120px}
  .v3{left:20px;top:418px;width:244px;height:243px}
  .t3{left:31px;top:392px;width:118px}
  .v4{left:545px;top:436px;width:245px;height:182px}
  .t4{left:548px;top:413px;width:127px}
  .v5{left:283px;top:550px;width:250px;height:225px}
  .t5{left:293px;top:522px;width:118px}

  .tagline{position:absolute;left:351px;top:387px;width:98px;text-align:center;color:var(--white);
    font-family:"Arimo",Arial,sans-serif;font-weight:700;font-size:18.5px;line-height:25px;white-space:nowrap}
</style>
</head>
<body>
<main class="poster">
  <div class="poster-field"></div>

  <header class="header">
    <div class="brand"><span class="brand-mark"></span><span class="brand-name">Keystone Aid Partners</span></div>
    <h1 class="title">OUR CORE VALUES</h1>
  </header>

  <div class="ghost-title">OUR CORE VALUES</div>
  <div class="footer-rule"></div>

  <svg class="connectors" width="810" height="810" viewBox="0 0 810 810" aria-hidden="true">
    <g fill="none" stroke="#ffffff" stroke-width="1.4">
      <polyline points="354,251 401,251 401,330"/>
      <polyline points="529,379 529,400 488,400"/>
      <polyline points="278,480 325,480 325,413"/>
      <polyline points="536,489 460,489 448,485"/>
      <polyline points="381,513 381,495 362,495"/>
    </g>
    <g fill="#ffffff">
      <circle cx="354" cy="251" r="4.5"/>
      <circle cx="529" cy="379" r="4.5"/>
      <circle cx="278" cy="480" r="4.5"/>
      <circle cx="536" cy="489" r="4.5"/>
      <circle cx="381" cy="513" r="4.5"/>
    </g>
    <polygon points="400,366 453,405 433,467 367,467 347,405" fill="#1f3a78" stroke="#0f1733" stroke-width="2"/>
    <defs>
      <polygon id="star" points="0,-22 5.2,-7 21,-6.8 8.4,2.7 13,18 0,9 -13,18 -8.4,2.7 -21,-6.8 -5.2,-7"/>
    </defs>
    <g fill="#2b3f7d" stroke="#ffffff" stroke-width="3">
      <use href="#star" x="401" y="341"/>
      <use href="#star" x="325" y="397"/>
      <use href="#star" x="476" y="397"/>
      <use href="#star" x="354" y="485"/>
      <use href="#star" x="447" y="485"/>
    </g>
  </svg>

  <div class="tagline">TO FIND<br>A BETTER<br>WAY</div>

  <section class="value v1">
    <h3>WHAT IT MEANS</h3>
    <p>Safety takes precedence over every phase of the day’s operation.</p>
    <h3>HOW TO EXPRESS IT</h3>
    <p>Anyone can call a stop to the work in progress if an unsafe act is occurring. In fact, it is each team member’s duty to do so, rectify the unsafe issue, then proceed. Never hesitate; everyone comes back. Finally, each after action review begins with discussing safety issues. We always let everyone on the team know of an unsafe situation, so it can be avoided in the future.</p>
    <h3>RESULT</h3>
    <p>All team members go home to their loved ones each day to pursue their individual happiness</p>
  </section>
  <div class="value-tab t1">Everyone comes back<br>to the Green Zone.</div>

  <section class="value v2">
    <h3>WHAT IT MEANS</h3>
    <p>We weave innovation into the fabric that makes up our company.</p>
    <h3>HOW TO EXPRESS IT</h3>
    <p>We’re early adopters of technology. We quickly evaluate new technologies or processes that could separate us from our competition. Then we implement and evaluate these new technologies. We dump it quickly if we see it is not helping us achieve “commander’s intent.” We have the guts to be first. We iterate continuously and attack, attack, attack.</p>
    <h3>RESULT</h3>
    <p>We will be ahead of our competition. It’s one mechanism that helps us scale. Prosperity favors the bold!</p>
  </section>
  <div class="value-tab t2">Boldly go.<br>Seek. Find.</div>

  <section class="value v3">
    <h3>WHAT IT MEANS</h3>
    <p>We always help your team members be successful. Commitment to each other and to our own personal integrity is the fuel that empowers us.</p>
    <h3>HOW TO EXPRESS IT</h3>
    <p>If a wingman is having challenges accomplishing their individual priorities or completing their assigned mission, volunteer to help them to do so. This goes for subs/suppliers as well. We help those who help us succeed! Always look to establish the best win-win relationship possible, and do what you can to support them if they get into a bind.</p>
    <h3>RESULT</h3>
    <p>Be there for them and they will be there for us.</p>
  </section>
  <div class="value-tab t3">Never leave your<br>wingman.</div>

  <section class="value v4">
    <h3>WHAT IT MEANS</h3>
    <p>No leader will put themselves ahead of their subordinates.</p>
    <h3>HOW TO EXPRESS IT</h3>
    <p>We lead by example. Demonstrate the moral courage and discipline to do the right thing at the highest level of quality.</p>
    <h3>RESULT</h3>
    <p>Every new team member’s will quickly realize their leaders genuinely care for their welfare and success. This is the best way to drive esprit de corps and achieve excellence.</p>
  </section>
  <div class="value-tab t4">Troops (Team Members)<br>eat first.</div>

  <section class="value v5">
    <h3>WHAT IT MEANS</h3>
    <p>If you’re not making mistakes, you’re not taking enough chances or getting out of your comfort zone.</p>
    <h3>HOW TO EXPRESS IT</h3>
    <p>Use your best judgment when trying something new. But, don’t let your pride keep you from saying, “I was wrong” when your idea doesn’t work. We trust you will know when it’s time to dump the idea, or stop doing something that doesn’t work.</p>
    <h3>RESULT</h3>
    <p>No one will ever be penalized for making a mistake. Don’t be afraid to try something you believe will work. That’s how we grow ourselves and our team members.</p>
  </section>
  <div class="value-tab t5">Fail quickly<br>and learn</div>
</main>
</body>
</html>
```